Tallbrook Sonic Group, Inc.
Project: Business Cards
Business Cards  - Health
Business Cards
Professional
2 Versions: Person 1. Marla Pennington, BSBA, BSDMS, RDMS Person 2. Gavin Pennington
Person 1. [no title] Person 2. Vice President, Sales
Ultrasound Services Sonographer Staffing PACS / Reporting
info@tallbrooksg.com
www.tallbrooksg.com
Member: CVRTB, NLUA & PSEK
Would prefer light color(s) or white background to match logo - no black backgrounds please. Let me know if you have any questions. Thanks!

```html
<!DOCTYPE html>
<html lang="en">
<head>
<meta charset="utf-8">
<title>Tallbrook Sonic Group, Inc. — Business Cards</title>
<link href="https://fonts.googleapis.com/css2?family=Jost:wght@400;500&display=swap" rel="stylesheet">
<style>
  :root {
    --stage: #3b3b3b;
    --card: #ffffff;
    --teal: #1b4b58;
    --teal-line: #2f6c7a;
    --ink: #3d4a52;
    --muted: #6b7479;
  }
  * { box-sizing: border-box; margin: 0; padding: 0; }
  html, body { width: 1200px; height: 901px; overflow: hidden; }
  body {
    background: var(--stage);
    font-family: "Jost", sans-serif;
    color: var(--ink);
    position: relative;
  }
  .card {
    position: absolute;
    background: var(--card);
    box-shadow: 0 6px 18px rgba(0,0,0,.35);
  }
  .card--front { left: 316px; top: 73px; width: 541px; height: 312px; }
  .card--back-a { left: 122px; top: 477px; width: 467px; height: 273px; }
  .card--back-b { left: 626px; top: 477px; width: 467px; height: 273px; }

  .wordmark {
    position: absolute;
    display: flex;
    align-items: center;
    gap: 8px;
    color: var(--teal);
    font-weight: 500;
    white-space: nowrap;
  }
  .wordmark__dot {
    width: 12px; height: 12px; border-radius: 50%;
    background: var(--teal);
  }
  .card--front .wordmark { left: 160px; top: 140px; font-size: 20px; }
  .card--back-a .wordmark, .card--back-b .wordmark { left: 110px; top: 36px; font-size: 19px; }

  .name-band {
    position: absolute;
    left: 0; right: 0; top: 100px; height: 48px;
    background: var(--teal);
    border-top: 2px solid var(--teal-line);
    border-bottom: 2px solid var(--teal-line);
    color: #fff;
    display: flex; flex-direction: column; justify-content: center; align-items: center;
    line-height: 1.2;
  }
  .name-band__name { font-size: 15px; font-weight: 500; }
  .name-band__creds { font-size: 11px; font-weight: 400; margin-left: 4px; }
  .name-band__title { font-size: 13px; }

  .details {
    position: absolute;
    left: 0; right: 0; top: 178px;
    display: flex; justify-content: center;
    font-size: 11px; line-height: 16px; color: var(--muted);
  }
  .services { text-align: right; padding-right: 12px; border-right: 1px solid #9aa3a7; }
  .contacts { padding-left: 12px; }
  .contact { display: flex; align-items: center; gap: 6px; }
  .contact svg { width: 9px; height: 9px; fill: var(--teal); flex: none; }
</style>
</head>
<body>

<section class="card card--front">
  <div class="wordmark"><span class="wordmark__dot"></span>Tallbrook Sonic Group, Inc.</div>
</section>

<section class="card card--back-a">
  <div class="wordmark"><span class="wordmark__dot"></span>Tallbrook Sonic Group, Inc.</div>
  <div class="name-band">
    <div><span class="name-band__name">Marla Pennington,</span><span class="name-band__creds">BSBA, BSDMS, RDMS</span></div>
  </div>
  <div class="details">
    <div class="services">Ultrasound Services<br>Sonographer Staffing<br>PACS / Reporting</div>
    <div class="contacts">
      <div class="contact"><svg viewBox="0 0 10 10"><path d="M2 0h2l1 3-1.5 1a6 6 0 0 0 2.5 2.5L7 5l3 1v2c0 1-1 2-2 2C4 10 0 6 0 2 0 1 1 0 2 0z"/></svg>(300)555-0142</div>
      <div class="contact"><svg viewBox="0 0 10 10"><path d="M0 2h10v6H0z"/></svg>info@tallbrooksg.com</div>
      <div class="contact"><svg viewBox="0 0 10 10"><circle cx="5" cy="5" r="5"/></svg>www.tallbrooksg.com</div>
    </div>
  </div>
</section>

<section class="card card--back-b">
  <div class="wordmark"><span class="wordmark__dot"></span>Tallbrook Sonic Group, Inc.</div>
  <div class="name-band">
    <div class="name-band__name">Gavin Pennington</div>
    <div class="name-band__title">Vice President, Sales</div>
  </div>
  <div class="details">
    <div class="services">Ultrasound Services<br>Sonographer Staffing<br>PACS / Reporting</div>
    <div class="contacts">
      <div class="contact"><svg viewBox="0 0 10 10"><path d="M2 0h2l1 3-1.5 1a6 6 0 0 0 2.5 2.5L7 5l3 1v2c0 1-1 2-2 2C4 10 0 6 0 2 0 1 1 0 2 0z"/></svg>(300)555-0142</div>
      <div class="contact"><svg viewBox="0 0 10 10"><path d="M0 2h10v6H0z"/></svg>info@tallbrooksg.com</div>
      <div class="contact"><svg viewBox="0 0 10 10"><circle cx="5" cy="5" r="5"/></svg>www.tallbrooksg.com</div>
    </div>
  </div>
</section>

</body>
</html>
```